Flyer Rework for Accountants and Lawyers

Information flyer for accountants and lawyers. Text and flowchart provided. Just need to make it look presentable for print and email. Needs to add logo (AI file provided) and provide graphics. No more than two pages. Our corporate visual identify guidelines are attached (MUST Use). Completed on both AI file and PPTX file.
Target Market(s)
Accountants, Company Directors and Lawyers
Industry/Entity Type
Finance And Accounting
Requirements
Must have
- Our corporate visual identify guidelines are attached (MUST Use)

```html
<!DOCTYPE html>
<html lang="en">
<head>
<meta charset="utf-8">
<title>Northbrook Advisory – Director Penalty Notices</title>
<link rel="stylesheet" href="https://fonts.googleapis.com/css2?family=Roboto:wght@400;500;700&family=Roboto+Condensed:wght@700&display=swap">
<style>
:root{
  --backdrop:#bcbdbf;
  --paper:#ffffff;
  --navy:#2e3a5c;
  --green:#8dc63f;
  --cyan:#63cbe0;
  --slate:#555b61;
  --grey-bar:#9a9b9d;
  --row:#f1f1f2;
  --row-alt:#e6e7e8;
  --box-dark:#54575b;
  --text:#3d4145;
}
*{box-sizing:border-box;margin:0;padding:0}
html,body{width:1200px;height:990px;overflow:hidden}
body{background:var(--backdrop);font-family:"Roboto",Arial,sans-serif;color:var(--text);position:relative}
.page{position:absolute;top:155px;width:525px;height:679px;background:var(--paper);box-shadow:0 1px 4px rgba(0,0,0,.25);overflow:hidden}
.page--front{left:63px}
.page--back{left:616px}
.abs{position:absolute}

/* brand */
.brand{display:flex;align-items:center;gap:8px}
.brand__square{width:12px;height:12px;background:var(--green)}
.brand__name{font-size:11px;font-weight:500;color:var(--slate);letter-spacing:.3px;white-space:nowrap}

.contact{right:30px;top:40px;font-size:11px;color:var(--slate);line-height:16px}
.contact__row{display:flex;align-items:center;gap:6px}
.contact__row--phone{font-weight:700}

.url-bar{left:0;top:88px;width:263px;height:30px;background:var(--grey-bar);color:#fff;font-size:9px;letter-spacing:3px;display:flex;align-items:center;padding-left:54px}
.hero-photo{left:0;top:103px;width:525px;height:190px;background:linear-gradient(90deg,#2c3950 0%,#6f7c8c 25%,#c8ccd2 55%,#eef0f2 75%,#f5f6f7 100%)}
.hero-claim{left:324px;top:158px;font-family:"Roboto Condensed","Arial Narrow",sans-serif;font-weight:700;font-size:20px;line-height:22px;color:var(--navy)}
.hero-claim .accent{color:var(--green)}
.intro-band{left:32px;top:269px;width:493px;height:56px;background:var(--navy);color:#fff;font-size:10px;line-height:12px;padding:10px 20px 0 32px}

.section-title{font-size:16px;font-weight:700;color:var(--green)}
.body-copy{font-size:9.6px;line-height:12px;color:var(--text)}
.body-copy p+p{margin-top:4px}

.facts{left:32px;top:439px;width:462px;border-collapse:collapse;font-size:8px;line-height:9.5px}
.facts th{background:var(--green);color:#fff;font-size:12px;font-weight:500;text-align:left;height:21px;padding:0 10px;border-right:2px solid #fff}
.facts td{padding:4px 10px;vertical-align:top;border-right:2px solid #fff}
.facts tr:nth-child(odd) td{background:var(--row)}
.facts tr:nth-child(even) td{background:var(--row-alt)}
.facts td.fact-name{width:152px;font-weight:700;color:#333}
.facts ul{margin:3px 0 0 20px}

.footer{left:0;top:655px;width:525px;height:24px;background:var(--cyan);color:var(--slate);font-size:9px;letter-spacing:2.5px;display:flex;align-items:center;justify-content:center}

/* back */
.tips-panel{left:0;top:0;width:525px;height:230px;background:var(--cyan)}
.tips-title{left:51px;top:36px;width:423px;height:29px;background:var(--navy);color:#fff;font-size:12px;font-weight:700;display:flex;align-items:center;justify-content:center}
.tips{left:58px;top:80px;width:420px;list-style:none;color:#fff;font-size:9.6px;line-height:11.5px}
.tips li{position:relative;padding-left:21px;margin-bottom:6px}
.tips li span{position:absolute;left:0;top:-1px;width:14px;height:14px;border:1px solid #fff;border-radius:50%;font-size:8px;text-align:center;line-height:12px}
.summary-tab{left:0;top:216px;width:252px;height:29px;background:var(--navy);color:#fff;font-size:16px;font-weight:700;padding-left:40px;display:flex;align-items:center}

.flow-lines{left:0;top:0}
.node{position:absolute;border-radius:5px;color:#fff;font-size:7px;line-height:8.2px;padding:10px 8px 0 14px}
.node--green{background:var(--green)}
.node--cyan{background:var(--cyan)}
.node--dark{background:var(--box-dark)}
.node ol{margin-left:10px}
.flow-label{position:absolute;font-size:8px;line-height:9px;font-weight:700;color:#333}

.help-bar{left:29px;top:482px;width:3px;height:56px;background:var(--slate)}
.help{left:38px;top:489px;width:450px}
.help .section-title{color:var(--cyan)}
.help .body-copy{margin-top:4px}
.call{left:0;top:553px;width:525px;text-align:center;font-size:10px;line-height:12px;color:var(--text)}
.call b{font-weight:700}
</style>
</head>
<body>

<section class="page page--front">
  <div class="brand abs" style="left:40px;top:36px">
    <div class="brand__square"></div>
    <div class="brand__name">NORTHBROOK ADVISORY</div>
  </div>
  <div class="contact abs">
    <div class="contact__row">
      <svg width="9" height="7" viewBox="0 0 9 7"><rect width="9" height="7" fill="#555b61"/><path d="M0 0l4.5 3.5L9 0" stroke="#fff" fill="none" stroke-width=".8"/></svg>
      info@nbadvisory.com.au
    </div>
    <div class="contact__row contact__row--phone">
      <svg width="9" height="9" viewBox="0 0 24 24"><path fill="#555b61" d="M6.6 10.8a15 15 0 006.6 6.6l2.2-2.2a1 1 0 011-.25 11.4 11.4 0 003.6.57 1 1 0 011 1V20a1 1 0 01-1 1A17 17 0 013 4a1 1 0 011-1h3.5a1 1 0 011 1c0 1.25.2 2.45.57 3.6a1 1 0 01-.25 1z"/></svg>
      (02) 5550 1234
    </div>
  </div>

  <div class="hero-photo abs" role="img" aria-label="Photo of two businessmen in suits reviewing documents together"></div>
  <div class="url-bar abs">www.nbadvisory.com.au</div>
  <div class="hero-claim abs">INDEPENDENT.<br><span class="accent">CONCISE.</span><br>EFFICIENT.</div>
  <div class="intro-band abs">Company directors and their advisors need to be aware that non-lodgement of Business Activities Statements (“BAS”) and Superannuation Guarantee Charge (“SCG”) Statements with the ATO may be personally liability for these debts.</div>

  <h2 class="section-title abs" style="left:35px;top:335px">Director Penalty Notices (“DPN”)</h2>
  <div class="body-copy abs" style="left:36px;top:362px;width:460px">
    <p>The ATO uses DPNs and Garnishee Notices to recovery tax debts and to impose positive obligations on Directors to deal with outstanding PAYG Withholding and the Superannuation Guarantee Charge debts (“Tax Debts”).</p>
    <p>The DPN regime makes directors of companies who fail to pay Tax Debts personally liable. The key facts of DPN regime are outlined below:</p>
  </div>

  <table class="facts abs">
    <thead><tr><th>Facts</th><th>Key facts of a Directors Penalty Notice</th></tr></thead>
    <tbody>
      <tr><td class="fact-name">1.&nbsp; Director personal liabilities</td><td>Directors become personally liable for Tax Debts 21 days are the DPN Notice is issued</td></tr>
      <tr><td class="fact-name">2.&nbsp; Automatic liability for unreported and unpaid Tax Debts</td><td>Where a company’s Tax Debts were both unreported and unpaid 3 months after the due date, the directors are automatically personally liable for the Tax Debts.</td></tr>
      <tr><td class="fact-name">3.&nbsp; Avoiding personal liability for directors once they receive a DPN</td><td>Within 21 days of issuing the DPN (which may be received a week or more after issue), a director can avoid personal liability by either:
        <ul><li>Paying the Tax Debt</li><li>Appointing an Administrator to the company</li><li>Appointing a Liquidator to the company.</li></ul></td></tr>
      <tr><td class="fact-name">4.&nbsp; Effect on new directors</td><td>New directors are liable if outstanding Tax Debts are unpaid 30 days after their appointment as director</td></tr>
      <tr><td class="fact-name">5.&nbsp; Time frames</td><td>ATO can only enforce a DPN after 21 days of giving notice to the director and notice can be given to the company tax agent</td></tr>
    </tbody>
  </table>

  <div class="footer abs">www.nbadvisory.com.au</div>
</section>

<section class="page page--back">
  <div class="tips-panel abs"></div>
  <div class="tips-title abs">TIPS FOR DIRECTORS TO LIMIT OR AVOID PERSONAL LIABILITY:</div>
  <ol class="tips abs">
    <li><span>1</span>Always lodge BAS and SGC Statements within 3 months of the due date, even if the liability cannot be paid!</li>
    <li><span>2</span>Act immediately upon receipt of a DPN and consider a payment arrangement with the ATO. This should be considered with care as payments made can be considered as preference payments to the ATO, if a liquidator is appointed. The ATO can make the directors personally liable for the ATO preference claim</li>
    <li><span>3</span>Seek professional advice from an insolvency practitioner about the options available and possibly save the company through a financial restructure.</li>
  </ol>
  <div class="summary-tab abs">Summary of the DPN</div>

  <svg class="flow-lines abs" width="525" height="679" viewBox="0 0 525 679">
    <defs><marker id="arrowhead" markerWidth="6" markerHeight="6" refX="5" refY="3" orient="auto"><path d="M0 0L6 3L0 6z" fill="#333"/></marker></defs>
    <g stroke="#333" stroke-width="1" fill="none">
      <path d="M126 364H148" marker-end="url(#arrowhead)"/>
      <path d="M191 310V268H305V283" marker-end="url(#arrowhead)"/>
      <path d="M191 423V467H305V447" marker-end="url(#arrowhead)"/>
      <path d="M348 316H369" marker-end="url(#arrowhead)"/>
      <path d="M441 357V376" marker-end="url(#arrowhead)"/>
      <path d="M391 357V417H349" marker-end="url(#arrowhead)"/>
    </g>
  </svg>
  <div class="flow-label" style="left:287px;top:272px">NO</div>
  <div class="flow-label" style="left:284px;top:453px">YES</div>
  <div class="flow-label" style="left:447px;top:362px">YES</div>
  <div class="flow-label" style="left:359px;top:404px">NO</div>

  <div class="node node--green" style="left:38px;top:329px;width:85px;height:69px;padding-top:18px">Issued Director’s Penalty Notice By ATO</div>
  <div class="node node--cyan" style="left:151px;top:310px;width:85px;height:113px;padding-top:19px">Business Activity Statement and Superannuation Guarantee Charge lodged within 3 months from due date</div>
  <div class="node node--dark" style="left:261px;top:286px;width:85px;height:69px;padding-top:16px;padding-left:13px">Director not personally liable yet.<br>(Have options)<br>[RIGHTS</div>
  <div class="node node--green" style="left:372px;top:265px;width:114px;height:92px;padding-top:13px;padding-left:17px">If Directors act within 21 days and:
    <ol><li>Wind up Company voluntarily; or</li><li>Appoint Voluntary Administrator; or</li><li>Pay debt in full</li></ol></div>
  <div class="node node--dark" style="left:261px;top:376px;width:85px;height:68px;padding-top:21px">Director Automatically personally liable</div>
  <div class="node node--green" style="left:401px;top:379px;width:85px;height:68px;padding-top:17px">Director not personally liable but the company is still insolvent.</div>

  <div class="help-bar abs"></div>
  <div class="help abs">
    <h2 class="section-title">How Northbrook Advisory can help?</h2>
    <div class="body-copy">Northbrook Advisory is a firm that specialises in insolvency and restructuring, we are here to assist your clients who experiencing financial difficulties with straight forward solutions in simple to understand terms.&nbsp; The initial consultation is free, strictly confidential and without obligation.</div>
  </div>
  <div class="call abs">Please call <b>(02) 5550 1234</b> to speak to one of our solvency specialistor<br>email <b>info@nbadvisory.com.au</b></div>

  <div class="brand abs" style="left:190px;top:607px">
    <div class="brand__square"></div>
    <div class="brand__name">NORTHBROOK ADVISORY</div>
  </div>

  <div class="footer abs">www.nbadvisory.com.au</div>
</section>

</body>
</html>
```